Social responsible Renewable Energy company

We at voltaQ are an independent power producer company founded in 2021 that handles large scale deployment of Renewable Energy and carbon neutral Energy as a service model. We offer turnkey solutions using solar panel systems and this could be incorporated in our business cards. You can also find our logo in the documents provided. Another key issue is that the business cards will be printed on recicled paper, not sure if this is a limitation in deciding the design. The recycled sign should also be added on the business card and stating that the paper used was recycled. Our website is www.myvoltaq.example. It should also be very professional, not too dreamy but still needs to capture your imagination. We are really excited to get your ideas !

Target Market(s)

Renewable Energy market

Contact Information for Business Card

The business card will be printed on recycled paper. Name of the company is voltaQ. Website is www.myvoltaq.example

Requirements
Nice to have
• Our motto: Powered by renewable, driven by people.

```html
<!DOCTYPE html>
<html lang="en">
<head>
<meta charset="utf-8">
<title>voltaQ business card</title>
<link rel="stylesheet" href="https://fonts.googleapis.com/css2?family=Montserrat:wght@500;600;700;800&display=swap">
<style>
  :root {
    --stage: #e9ebee;
    --paper: #ffffff;
    --navy: #1d4d7b;
    --blue: #3580c4;
    --ink: #1b1d22;
    --shadow: rgba(20, 30, 45, 0.18);
  }
  * { box-sizing: border-box; margin: 0; padding: 0; }
  html, body { width: 1200px; height: 780px; overflow: hidden; }
  body {
    background: var(--stage);
    font-family: "Montserrat", sans-serif;
    color: var(--ink);
  }
  .sheet {
    position: relative;
    width: 1200px;
    height: 780px;
    display: flex;
    align-items: center;
    justify-content: center;
    gap: 50px;
  }
  .card {
    position: relative;
    width: 540px;
    height: 308px;
    border-radius: 26px;
    background: var(--paper);
    overflow: hidden;
    box-shadow: 0 14px 30px var(--shadow);
  }

  /* Front */
  .card-front .band {
    position: absolute;
    left: 0; right: 0; bottom: 0;
    height: 144px;
    background: linear-gradient(180deg, var(--navy) 0%, var(--blue) 100%);
  }
  .card-front .wordmark {
    position: absolute;
    left: 0; right: 0;
    top: 78px;
    text-align: center;
    font-weight: 800;
    font-size: 74px;
    letter-spacing: 1px;
    color: var(--navy);
    line-height: 1;
  }
  .card-front .site {
    position: absolute;
    left: 0; right: 0;
    top: 196px;
    text-align: center;
    font-weight: 500;
    font-size: 12px;
    letter-spacing: 7px;
    color: var(--paper);
  }

  /* Back */
  .card-back .side-panel {
    position: absolute;
    left: 0; top: 0; bottom: 0;
    width: 236px;
    background: linear-gradient(180deg, var(--navy) 0%, var(--navy) 45%, var(--blue) 100%);
  }
  .card-back .side-panel .wordmark {
    position: absolute;
    left: 28px;
    top: 30px;
    font-weight: 800;
    font-size: 34px;
    color: var(--paper);
    line-height: 1;
  }
  .card-back .identity {
    position: absolute;
    left: 268px;
    top: 40px;
  }
  .card-back .name {
    font-weight: 800;
    font-size: 31px;
    color: var(--blue);
    line-height: 1.05;
  }
  .card-back .role {
    margin-top: 4px;
    font-weight: 600;
    font-size: 9.5px;
    letter-spacing: 2.4px;
    color: var(--ink);
  }
  .card-back .contacts {
    position: absolute;
    left: 268px;
    top: 166px;
    list-style: none;
  }
  .card-back .contacts li {
    display: flex;
    align-items: center;
    gap: 10px;
    font-weight: 500;
    font-size: 11px;
    line-height: 1.3;
    margin-bottom: 9px;
  }
  .card-back .contacts .icon {
    flex: none;
    width: 19px;
    height: 19px;
    border-radius: 50%;
    background: var(--navy);
    display: flex;
    align-items: center;
    justify-content: center;
  }
  .card-back .contacts svg { width: 11px; height: 11px; }
</style>
</head>
<body>
<main class="sheet">

  <section class="card card-front" aria-label="Card front">
    <div class="band"></div>
    <div class="wordmark">voltaQ</div>
    <div class="site">www.myvoltaq.example</div>
  </section>

  <section class="card card-back" aria-label="Card back">
    <div class="side-panel">
      <div class="wordmark">voltaQ</div>
    </div>

    <div class="identity">
      <h1 class="name">Daniel Reyes</h1>
      <p class="role">MANAGING DIRECTOR</p>
    </div>

    <ul class="contacts">
      <li>
        <span class="icon">
          <svg viewBox="0 0 24 24" fill="#fff"><path d="M6.6 10.8a15.1 15.1 0 0 0 6.6 6.6l2.2-2.2a1 1 0 0 1 1-.25 11.4 11.4 0 0 0 3.6.57 1 1 0 0 1 1 1V20a1 1 0 0 1-1 1A17 17 0 0 1 3 4a1 1 0 0 1 1-1h3.5a1 1 0 0 1 1 1c0 1.25.2 2.45.57 3.57a1 1 0 0 1-.25 1z"/></svg>
        </span>
        555-014-2290
      </li>
      <li>
        <span class="icon">
          <svg viewBox="0 0 24 24" fill="none" stroke="#fff" stroke-width="2.2"><rect x="3" y="6" width="18" height="12" rx="1.5"/><path d="M3.5 6.5 12 13l8.5-6.5"/></svg>
        </span>
        d.reyes@voltaq.example
      </li>
      <li>
        <span class="icon">
          <svg viewBox="0 0 24 24" fill="#fff"><path d="M12 2a7 7 0 0 0-7 7c0 5.2 7 13 7 13s7-7.8 7-13a7 7 0 0 0-7-7zm0 9.5A2.5 2.5 0 1 1 12 6.5a2.5 2.5 0 0 1 0 5z"/></svg>
        </span>
        <span>418 Cedar Ridge Road, Tempe<br>Sun Valley, Arizona 85281</span>
      </li>
      <li>
        <span class="icon">
          <svg viewBox="0 0 24 24" fill="none" stroke="#fff" stroke-width="1.8"><circle cx="12" cy="12" r="9"/><path d="M3 12h18M12 3c2.6 2.6 2.6 15.4 0 18M12 3c-2.6 2.6-2.6 15.4 0 18"/></svg>
        </span>
        www.myvoltaq.example
      </li>
    </ul>
  </section>

</main>
</body>
</html>
```